Velno Recycling needs a new web design

We need a new web design for our company based in Austin, TX. We resell and recycling electronics such as laptops, computer components, Tovlets, Brunos, etc. Since our inception over ten years ago, we’ve become one of the premier electronics recycling and remarketing companies in Austin, Texas.

```html
<!DOCTYPE html>
<html lang="en">
<head>
<meta charset="utf-8">
<title>Velno Recycling</title>
<link href="https://fonts.googleapis.com/css2?family=Poppins:wght@300;400;500;600;700&display=swap" rel="stylesheet">
<style>
:root{
  --navy:#16356b;
  --blue:#1e9fdc;
  --ink:#222;
  --muted:#555;
  --green-dark:#1f5d2a;
  --green-mid:#5ea53a;
  --green-light:#8cc253;
  --band:#d6dde4;
  --white:#fff;
  --rule:#d9d9d9;
}
*{margin:0;padding:0;box-sizing:border-box}
html,body{width:1200px;height:1200px;overflow:hidden;background:var(--white);font-family:'Poppins',sans-serif;color:var(--ink)}
.page{position:relative;width:1200px;height:1200px}
.abs{position:absolute}

/* header */
.brand{left:160px;top:22px;display:flex;align-items:center;gap:7px}
.brand-dot{width:26px;height:26px;border-radius:50%;background:var(--navy)}
.brand-name{font-size:14px;font-weight:600;color:var(--navy);white-space:nowrap}
.nav{top:30px;font-size:11px;font-weight:400;color:#333;letter-spacing:.2px;white-space:nowrap}
.phone{right:232px;top:28px;font-size:11px;color:#444;white-space:nowrap}
.phone b{font-weight:600;color:#111}
.toll{right:236px;top:44px;font-size:8.5px;font-weight:600;color:var(--blue)}
.divider{left:982px;top:28px;width:1px;height:16px;background:#ccc}

/* hero */
.hero{left:0;top:72px;width:1200px;height:510px;
  background:radial-gradient(ellipse 55% 70% at 50% 50%,var(--green-light) 0%,var(--green-mid) 55%,var(--green-dark) 100%)}
.hero-photo{left:536px;top:184px;width:384px;height:398px;
  background:radial-gradient(ellipse at 50% 60%,#5d6b55 0%,#6e9a4c 55%,rgba(110,165,70,0) 75%)}
.kicker{left:252px;top:259px;font-size:11px;font-weight:500;color:var(--white)}
.hero-title{left:251px;top:278px;font-size:45px;font-weight:700;line-height:43px;color:var(--white);letter-spacing:-.5px}
.hero-lead{left:251px;top:384px;width:200px;font-size:11px;line-height:17px;font-weight:300;color:var(--white)}
.stat{left:888px;top:256px;width:160px;text-align:center;font-size:10.5px;line-height:15px;font-weight:300;color:var(--white)}
.stat b{font-weight:600}
.arrow{width:31px;height:31px;border:1.5px solid var(--white);border-radius:50%;top:312px}
.arrow svg{position:absolute;left:9px;top:9px}
.card{left:214px;top:455px;width:248px;height:127px;background:var(--white);box-shadow:0 6px 14px rgba(0,0,0,.12)}
.card p{position:absolute;left:37px;top:23px;font-size:10.5px;line-height:17px;font-weight:300;color:#444;white-space:nowrap}
.card p b{font-weight:600;color:#222}
.btn{border:3px solid var(--blue);background:var(--white);font-size:10.5px;font-weight:500;color:#333;display:flex;align-items:center;justify-content:space-between;padding:0 12px}
.btn span.chev{color:var(--blue);font-size:10px}
.card .btn{position:absolute;left:37px;top:69px;width:135px;height:36px}

/* features */
.feature{top:644px;width:248px}
.feature-icon{position:absolute;left:0;top:0}
.feature-title{position:absolute;left:52px;top:1px;font-size:13.5px;font-weight:600;line-height:15px;color:#2a2a2a;white-space:nowrap}
.feature-text{position:absolute;left:0;top:50px;width:240px;font-size:10.3px;line-height:17px;font-weight:300;color:#444;white-space:nowrap}
.feature-rule{position:absolute;left:0;top:101px;width:248px;height:1px;background:var(--rule)}
.feature-rule.active{background:var(--blue)}
.feature-link{position:absolute;left:0;top:112px;font-size:11px;font-weight:500;color:var(--blue)}

/* about */
.about-title{left:0;top:860px;width:1200px;text-align:center;font-size:22px;font-weight:600;color:#222}
.about-text{left:250px;top:908px;width:700px;text-align:center;font-size:12px;line-height:21px;font-weight:300;color:#555;white-space:nowrap}
.about-btn{left:533px;top:994px;width:134px;height:36px}

/* capability band */
.band{left:0;top:1083px;width:1200px;height:117px;background:var(--band)}
.band-title{left:0;top:1126px;width:1200px;text-align:center;font-size:22px;font-weight:600;color:#222}
</style>
</head>
<body>
<div class="page">

  <header>
    <div class="abs brand"><span class="brand-dot"></span><span class="brand-name">Velno Recycling</span></div>
    <nav>
      <span class="abs nav" style="left:348px">HOME</span>
      <span class="abs nav" style="left:406px">SERVICES <svg width="7" height="5" viewBox="0 0 7 5" style="margin-left:4px"><path d="M1 1l2.5 2.5L6 1" fill="none" stroke="#333" stroke-width="1"/></svg></span>
      <span class="abs nav" style="left:480px">ABOUT</span>
      <span class="abs nav" style="left:542px">CONTACT</span>
    </nav>
    <div class="abs phone">(844)55-<b>VELNO</b> (83566)</div>
    <div class="abs toll">TOLL FREE</div>
    <div class="abs divider"></div>
    <svg class="abs" style="left:996px;top:30px" width="13" height="13" viewBox="0 0 13 13"><circle cx="5" cy="5" r="3.8" fill="none" stroke="#555" stroke-width="1.8"/><path d="M8 8l4 4" stroke="#555" stroke-width="2"/></svg>
    <svg class="abs" style="left:1026px;top:30px" width="13" height="12" viewBox="0 0 13 12"><path d="M0 1.5h13M0 6h13M0 10.5h13" stroke="#555" stroke-width="2"/></svg>
  </header>

  <section class="abs hero"></section>
  <div class="abs hero-photo" role="img" aria-label="Green wheelie bin overflowing with discarded computers, towers and circuit boards"></div>
  <div class="abs kicker">Electronic waste recycling</div>
  <h1 class="abs hero-title">ONE STOP<br>SHOP.</h1>
  <p class="abs hero-lead">Premier electronics recycling<br>and remarketing companies in<br>Austin, Texas.</p>
  <p class="abs stat">Electronic waste represents <b>2% of America's trash</b> in landfills, but it equals <b>70%</b> of overall toxic waste.</p>
  <div class="abs arrow" style="left:30px"><svg width="10" height="10" viewBox="0 0 10 10"><path d="M6.5 1.5L3 5l3.5 3.5" fill="none" stroke="#fff" stroke-width="1.3"/></svg></div>
  <div class="abs arrow" style="left:1139px"><svg width="10" height="10" viewBox="0 0 10 10"><path d="M3.5 1.5L7 5 3.5 8.5" fill="none" stroke="#fff" stroke-width="1.3"/></svg></div>
  <div class="abs card">
    <p>Providing a full <b>“chain of custody”</b><br>on electronic waste recycling.</p>
    <div class="btn">How It Works <span class="chev">›</span></div>
  </div>

  <section>
    <div class="abs feature" style="left:214px">
      <svg class="feature-icon" width="38" height="38" viewBox="0 0 38 38"><g fill="none" stroke="#3fa535" stroke-width="5" stroke-linecap="round"><path d="M12 11l5-7h4l5 7"/><path d="M32 22l3 7-2 4h-9"/><path d="M14 33H6l-2-4 4-7"/></g><g fill="#3fa535"><path d="M24 9l6 1-2 6z"/><path d="M22 29l-4 4 4 4z"/><path d="M8 19l-5-3 7-2z"/></g></svg>
      <div class="feature-title">eWaste<br>Recycling</div>
      <p class="feature-text">Electronic waste recycling and electronics<br>remarketing program for customers.</p>
      <div class="feature-rule active"></div>
      <div class="feature-link">Details &nbsp;›</div>
    </div>
    <div class="abs feature" style="left:476px">
      <svg class="feature-icon" width="38" height="38" viewBox="0 0 38 38"><path d="M1 0h20l8 8v30H1z" fill="#1a73c4"/><path d="M21 0v8h8z" fill="#fff"/><path d="M22 0v7h7" fill="#1a73c4" opacity=".6"/></svg>
      <div class="feature-title">Data<br>Destruction</div>
      <p class="feature-text">Data Destruction with our state of the<br>art Degaussing equipment.</p>
      <div class="feature-rule"></div>
      <div class="feature-link">Details &nbsp;›</div>
    </div>
    <div class="abs feature" style="left:738px">
      <svg class="feature-icon" width="38" height="38" viewBox="0 0 38 38"><path d="M1 2h33v15c0 10-8 17-16.5 20C9 34 1 27 1 17z" fill="#1a73c4"/><path d="M8 17l7 7 12-13" fill="none" stroke="#fff" stroke-width="4"/></svg>
      <div class="feature-title">Global Logistics<br>Support</div>
      <p class="feature-text">Care about keeping our clients recycle<br>and remarketing equipment safe.</p>
      <div class="feature-rule"></div>
      <div class="feature-link">Details &nbsp;›</div>
    </div>
  </section>

  <section>
    <h2 class="abs about-title">Velno Recycling</h2>
    <p class="abs about-text">We started Velno Recycling in 2006 to fill the void as a full service computer and electronic waste<br>recycling “one stop shop.” Since our inception over ten years ago, we’ve become one of the premier<br>electronics recycling and remarketing companies in Austin, Texas.</p>
    <div class="abs btn about-btn">Learn More <span class="chev">›</span></div>
  </section>

  <section class="abs band"></section>
  <h2 class="abs band-title">Capability Overview</h2>

</div>
</body>
</html>
```